Hot-air ballooning company needs a DL-size flyer

Skylark Aerial Tours is a hot-air ballooning company which flies passengers in the King Valley, Victoria, Australia.
We need a 2-sided DL-size flyer which promotes our hot-air balloon flights and packages.
Most of our customers are couples, and we want the flyer design to communicate safety, adventure, and romance.
The flyer should make the best use of our images which we provide, and we've also included a document with the text for the flyer.
Updates

2 days is not long enough to gather designs, the brief never asked me what my deadline should be.

Target Market(s)

Couples, buyers are majority female, between the ages of 20-60

Industry/Entity Type

Tourism

Font styles to use
Sans Serif

Colors

Designer to choose colors to be used in the design.

Requirements
Must have
• Communicate safety, adventure, and romance
• Use images
Nice to have
• There is a lot of text, it would be great if you could make it look like as little text as possible
Should not have
• No childish designs

```html
<!DOCTYPE html>
<html lang="en">
<head>
<meta charset="utf-8">
<title>King Valley Hot-Air Ballooning – DL Flyer</title>
<link rel="stylesheet" href="https://fonts.googleapis.com/css2?family=Marcellus&family=Alegreya+Sans:ital,wght@0,400;0,500;0,700;1,400&display=swap">
<style>
:root{
  --stage:#e9e6e2;
  --orange:#f39a1e;
  --amber:#f7b733;
  --tangerine:#ef7a1a;
  --red:#e63b18;
  --deep-red:#b31d0f;
  --maroon:#7d140a;
  --ink:#3a1a0c;
  --white:#ffffff;
}
*{box-sizing:border-box;margin:0;padding:0}
html,body{width:1200px;height:900px;overflow:hidden}
body{background:var(--stage);font-family:"Alegreya Sans",sans-serif;position:relative}
.panel{position:absolute;top:22px;width:426px;height:855px;overflow:hidden;box-shadow:0 2px 10px rgba(0,0,0,.25)}
.panel--front{left:170px}
.panel--back{left:638px}
.panel__art{position:absolute;inset:0;width:426px;height:855px}
.txt{position:absolute;color:var(--white);line-height:1.3;letter-spacing:.3px}
.dropcap{float:left;font-size:40px;line-height:.8;margin:2px 3px 0 0}

.brand-title{left:0;width:426px;top:38px;text-align:center;font-family:"Marcellus",serif;text-shadow:0 2px 6px rgba(0,0,0,.35);letter-spacing:0}
.brand-title__main{display:block;font-size:54px;letter-spacing:1px;line-height:1}
.brand-title__sub{display:block;font-size:29px;letter-spacing:1.5px;margin-top:6px}
.ribbon{left:38px;top:330px;height:20px;line-height:20px;font-family:"Marcellus",serif;font-size:13.5px;letter-spacing:.2px;transform:rotate(-12.8deg);transform-origin:left bottom;white-space:nowrap}

.intro{left:26px;top:376px;width:226px;font-size:17.5px;line-height:1.2;color:var(--ink)}
.mountains{left:62px;top:508px;width:345px;font-size:17.5px;line-height:1.2}
.romance{left:206px;top:578px;width:190px;font-size:17px;line-height:1.22}
.romance__cta{display:block;font-weight:700;margin-top:6px}
.romance__cta i{font-weight:400}
.bookings{right:28px;top:780px;text-align:right;font-size:14.5px;line-height:1.35;letter-spacing:0}
.bookings__label{font-family:"Marcellus",serif;font-size:15px;letter-spacing:.8px;font-weight:700}

.location{left:32px;top:48px;width:215px;font-size:16.5px;line-height:1.2}
.location__note{display:block;margin-top:8px}
.flight{left:30px;top:216px;width:380px;color:var(--ink)}
.flight__title{font-size:24px;font-weight:700;letter-spacing:.5px;margin-bottom:4px}
.flight__list{list-style:none;font-size:17px;line-height:20.5px;width:375px}
.flight__list li{position:relative;padding-left:25px;padding-right:10px}
.flight__list li::before{content:"";position:absolute;left:5px;top:5px;width:4px;height:8px;border:solid var(--ink);border-width:0 1.6px 1.6px 0;transform:rotate(40deg)}
.social{left:30px;top:690px;font-size:15px}
.social__row{display:flex;align-items:center;gap:8px;margin-top:8px}
.social__dot{width:22px;height:22px;border-radius:50%;background:var(--amber)}
.licence{left:30px;top:820px;width:385px;font-size:12.5px;line-height:1.2;letter-spacing:0}
</style>
</head>
<body>

<section class="panel panel--front">
  <svg class="panel__art" viewBox="0 0 426 855">
    <defs>
      <linearGradient id="heroSky" x1="0" y1="0" x2="0" y2="1">
        <stop offset="0" stop-color="#6fa3d6"/><stop offset=".4" stop-color="#b9cbdc"/>
        <stop offset=".6" stop-color="#c8ccce"/><stop offset=".8" stop-color="#6e7458"/><stop offset="1" stop-color="#4e4a36"/>
      </linearGradient>
      <linearGradient id="valleySky" x1="0" y1="0" x2="0" y2="1">
        <stop offset="0" stop-color="#79a9d8"/><stop offset=".6" stop-color="#c9d3dc"/><stop offset="1" stop-color="#6f6a55"/>
      </linearGradient>
      <linearGradient id="coupleTone" x1="0" y1="0" x2="1" y2="1">
        <stop offset="0" stop-color="#e9e2d0"/><stop offset=".5" stop-color="#b6805d"/><stop offset="1" stop-color="#cfd4de"/>
      </linearGradient>
    </defs>
    <rect width="426" height="855" fill="var(--orange)"/>
    <polygon points="0,0 426,0 426,262 0,350" fill="url(#heroSky)" role="img" aria-label="Photo: hot-air balloons over a misty King Valley winery at sunrise"/>
    <polygon points="0,300 70,360 0,380" fill="var(--amber)"/>
    <polygon points="30,352 426,262 426,296 130,348" fill="var(--maroon)"/>
    <polygon points="130,348 300,318 205,345" fill="var(--red)"/>
    <polygon points="0,380 210,345 300,520 0,540" fill="var(--tangerine)"/>
    <polygon points="205,345 426,318 426,500 295,522" fill="url(#valleySky)" role="img" aria-label="Photo: colourful balloons above fog-covered hills"/>
    <polygon points="0,540 40,510 426,488 426,600 0,610" fill="var(--red)"/>
    <polygon points="0,555 30,600 0,600" fill="var(--amber)"/>
    <rect x="0" y="598" width="426" height="200" fill="var(--red)"/>
    <rect x="0" y="575" width="185" height="215" fill="url(#coupleTone)" role="img" aria-label="Photo: smiling couple embracing outdoors"/>
    <polygon points="0,800 426,758 426,855 0,855" fill="var(--deep-red)"/>
    <polygon points="0,720 40,800 0,805" fill="var(--amber)"/>
  </svg>

  <h1 class="txt brand-title"><span class="brand-title__main">KING VALLEY</span><span class="brand-title__sub">HOT-AIR BALLOONING</span></h1>
  <p class="txt ribbon">THE PERFECT GOURMET BALLOONING EXPERIENCE</p>
  <p class="txt intro"><span class="dropcap">F</span>rom the vineyards and patchwork of fields the views expand to the Ovens River, spectacular Mt Buffalo and the High Country beyond</p>
  <p class="txt mountains"><span class="dropcap">T</span>he mountain views, once aloft, come to life in dramatic 3D with the early morning light</p>
  <p class="txt romance">Live the romance and adventure of flying the beautiful King Valley and surrounds in a hot-air balloon at dawn.
    <span class="romance__cta">Celebrate your flight with a delicious breakfast afterwards <i>(optional)</i></span></p>
  <p class="txt bookings"><span class="bookings__label">BOOKINGS/MORE INFORMATION:</span><br>www.skylarkaerialtours.com.au<br>flights@skylarkaerialtours.com.au or call us on 1300 759 275</p>
</section>

<section class="panel panel--back">
  <svg class="panel__art" viewBox="0 0 426 855">
    <defs>
      <linearGradient id="basketTone" x1="0" y1="0" x2="0" y2="1">
        <stop offset="0" stop-color="#3c2a22"/><stop offset=".5" stop-color="#8a6a4c"/><stop offset="1" stop-color="#a48a62"/>
      </linearGradient>
      <linearGradient id="glowTone" x1="0" y1="0" x2="0" y2="1">
        <stop offset="0" stop-color="#c9391c"/><stop offset=".35" stop-color="#f6a42a"/><stop offset=".7" stop-color="#3e4a5c"/><stop offset="1" stop-color="#2a2a30"/>
      </linearGradient>
    </defs>
    <rect width="426" height="855" fill="var(--orange)"/>
    <polygon points="0,0 426,0 426,210 0,188" fill="var(--red)"/>
    <polygon points="0,0 30,0 0,60" fill="var(--white)"/>
    <polygon points="262,0 426,0 426,190 300,200" fill="url(#basketTone)" role="img" aria-label="Photo: passengers waving from a balloon basket under the burner"/>
    <polygon points="370,210 426,150 426,220" fill="var(--white)"/>
    <polygon points="260,520 426,500 426,800 300,790" fill="url(#glowTone)" role="img" aria-label="Photo: glowing balloon being inflated at dawn with onlookers"/>
    <polygon points="0,600 30,690 0,700" fill="var(--white)"/>
    <polygon points="0,690 300,660 260,780 0,820" fill="var(--red)"/>
    <polygon points="240,780 320,720 340,790" fill="var(--amber)"/>
    <polygon points="0,815 426,800 426,855 0,855" fill="var(--deep-red)"/>
  </svg>

  <p class="txt location"><span class="dropcap" style="font-size:38px">M</span>ilawa is conveniently located less than an hour's drive from most places in Victoria's North East and Albury in NSW<span class="location__note">Mansfield flights are also available</span></p>

  <div class="txt flight">
    <h2 class="flight__title">YOUR FLIGHT</h2>
    <ul class="flight__list">
      <li>One-hour sunrise balloon flight in the spectacular King Valley region in North East Victoria</li>
      <li>Delicious champagne breakfast after the flight (recommended option)</li>
      <li>Informative details throughout your experience with our locally based expert crew</li>
      <li>The opportunity to be involved in the inflation and deflation process should you wish</li>
      <li>Safe, friendly and professional</li>
      <li>The flight lasts approximately 1 hour</li>
      <li>The entire experience takes about 3-4 hours</li>
      <li>Suitable from age 7 to 97</li>
      <li>Gift Vouchers are also available</li>
      <li>Contact us for exclusive flight options at your custom location</li>
    </ul>
  </div>

  <div class="txt social">Find us
    <div class="social__row"><span class="social__dot"></span><span>@skylarkaerialtours</span></div>
  </div>
  <p class="txt licence">Skylark Aerial Tours operates under Air Operator's Certificate C481736-02 issued by the National Air Safety Regulator</p>
</section>

</body>
</html>
```